Business card design for upmarket Home Technology design and Installation company

Hello designers, we need a great business card designed.
We need it to convey high tech, and also sophistication .
We work with some of the most affluent people in the world building them home technology systems, and A/V entertainment systems.

Services offered include the following:
Design, sales, installation, and maintenance of

*Home Automation systems
*Distributed / Multi-Room Audio and Video
*High Performance Networks & WiFi
* Lighting and Shade Control
*Home cinema
*Security and CCTV Systems

I have included a copy of our logo to use for your design efforts.

Target Market(s)

Upmarket clients with multi million euro villas.

Industry/Entity Type

Home technology

Contact Information for Business Card

NAME: Derek Halvin ADDRESS: Carrer Bellamar Local 42, Cala Torrent, 07293 PHONE: +34-652-918-204 EMAIL: DHalvin@VORTELhomesystems.example WEB: www.vortelhomesystems.example

Requirements
Must have
• Our Logo, and our tagline

```html
<!DOCTYPE html>
<html lang="en">
<head>
<meta charset="utf-8">
<title>VORTEL Home Systems – Business Card</title>
<link rel="stylesheet" href="https://fonts.googleapis.com/css2?family=Roboto:wght@500;700&family=Nunito+Sans:wght@400&display=swap">
<style>
  :root {
    --backdrop: #4a4947;
    --card-dark: #262523;
    --card-mid: #2d2c29;
    --gold: #c9a45c;
    --gold-soft: #b89550;
    --text-light: #ece9e2;
  }
  * { margin: 0; padding: 0; box-sizing: border-box; }
  html, body { width: 1200px; height: 900px; overflow: hidden; }
  body {
    background: radial-gradient(ellipse at 40% 30%, #52504d 0%, var(--backdrop) 60%, #434240 100%);
    position: relative;
  }
  .card {
    position: absolute;
    left: 393px;
    width: 414px;
    height: 238px;
    background: linear-gradient(135deg, var(--card-mid) 0%, var(--card-dark) 100%);
    overflow: hidden;
  }
  .card--services { top: 195px; }
  .card--contact { top: 495px; }

  .services-title {
    position: absolute; left: 19px; top: 26px;
    font: 700 13px/1 "Roboto", sans-serif;
    color: var(--gold); letter-spacing: 0.4px;
  }
  .service-steps { position: absolute; left: 23px; top: 49px; list-style: none; }
  .service-steps li {
    display: flex; align-items: center; gap: 6px;
    height: 15px;
    font: 500 10px/1 "Roboto", sans-serif; color: var(--gold);
  }
  .service-steps li::before {
    content: ""; width: 5px; height: 5px; border-radius: 50%;
    background: var(--gold);
  }
  .system-list {
    position: absolute; left: 23px; top: 118px; list-style: none;
    font: 400 8.5px/1.15 "Nunito Sans", sans-serif; color: var(--text-light);
  }
  .system-list li { position: relative; padding-left: 5px; margin-bottom: 4.6px; }
  .system-list li::before { content: "•"; position: absolute; left: 0; }

  .brand-name {
    position: absolute; width: 130px; text-align: center;
    font: 500 18px/1 "Roboto", sans-serif; color: var(--gold);
    letter-spacing: 3px;
  }
  .card--services .brand-name { left: 265px; top: 140px; }
  .card--contact .brand-name { left: 252px; top: 135px; }

  .holder-name {
    position: absolute; left: 17px; top: 96px;
    font: 700 20px/1 "Roboto", sans-serif; color: var(--gold);
  }
  .contact-list { position: absolute; left: 26px; top: 133px; list-style: none; }
  .contact-list li {
    display: flex; align-items: flex-start; gap: 10px;
    font: 400 8.8px/1.1 "Nunito Sans", sans-serif; color: var(--text-light);
    margin-bottom: 7px;
  }
  .contact-list svg { flex: none; width: 8px; height: 8px; fill: var(--gold); margin-top: 1px; }
</style>
</head>
<body>
  <section class="card card--services">
    <h2 class="services-title">SERVICES OFFERED</h2>
    <ul class="service-steps">
      <li>Design</li>
      <li>Sales</li>
      <li>Installation</li>
      <li>Maintenance of</li>
    </ul>
    <ul class="system-list">
      <li>Home Automation systems</li>
      <li>Distributed / Multi-Room<br>Audio and Video</li>
      <li>High Performance Networks &amp; WiFi</li>
      <li>Lighting and Shade Control</li>
      <li>Home cinema</li>
      <li>Security and CCTV Systems</li>
    </ul>
    <div class="brand-name">VORTEL</div>
  </section>

  <section class="card card--contact">
    <h1 class="holder-name">Derek Halvin</h1>
    <ul class="contact-list">
      <li>
        <svg viewBox="0 0 24 24"><path d="M6.6 10.8a15 15 0 0 0 6.6 6.6l2.2-2.2a1 1 0 0 1 1-.25 11.4 11.4 0 0 0 3.6.57 1 1 0 0 1 1 1V20a1 1 0 0 1-1 1A17 17 0 0 1 3 4a1 1 0 0 1 1-1h3.5a1 1 0 0 1 1 1c0 1.25.2 2.45.57 3.57a1 1 0 0 1-.25 1z"/></svg>
        <span>+34-652-918-204</span>
      </li>
      <li>
        <svg viewBox="0 0 24 24"><path d="M2 5h20v14H2z M2 5l10 8 10-8" /></svg>
        <span>DHalvin@VORTELhomesystems.example</span>
      </li>
      <li>
        <svg viewBox="0 0 24 24"><path d="M12 2a7 7 0 0 0-7 7c0 5.25 7 13 7 13s7-7.75 7-13a7 7 0 0 0-7-7zm0 9.5A2.5 2.5 0 1 1 12 6.5a2.5 2.5 0 0 1 0 5z"/></svg>
        <span>Carrer Bellamar Local 42, Cala<br>Torrent, 07293</span>
      </li>
      <li>
        <svg viewBox="0 0 24 24"><path d="M12 2a10 10 0 1 0 0 20 10 10 0 0 0 0-20zm6.9 6h-2.9a15.6 15.6 0 0 0-1.4-3.6A8 8 0 0 1 18.9 8zM12 4c.8 1.2 1.5 2.5 1.9 4h-3.8c.4-1.5 1.1-2.8 1.9-4zM4.3 14a8.2 8.2 0 0 1 0-4h3.4a16 16 0 0 0 0 4zm.8 2h2.9c.3 1.3.8 2.5 1.4 3.6A8 8 0 0 1 5.1 16zM8 8H5.1a8 8 0 0 1 4.3-3.6C8.8 5.5 8.3 6.7 8 8zm4 12c-.8-1.2-1.5-2.5-1.9-4h3.8c-.4 1.5-1.1 2.8-1.9 4zm2.3-6H9.7a14.7 14.7 0 0 1 0-4h4.6a14.7 14.7 0 0 1 0 4zm.3 5.6c.6-1.1 1.1-2.3 1.4-3.6h2.9a8 8 0 0 1-4.3 3.6zm1.7-5.6a16 16 0 0 0 0-4h3.4a8.2 8.2 0 0 1 0 4z"/></svg>
        <span>www.vortelhomesystems.example</span>
      </li>
    </ul>
    <div class="brand-name">VORTEL</div>
  </section>
</body>
</html>
```